Lumoravex Web Design for Digital Marketing Agency

Please build us a web page for our digital and software consulting company
Please use these websites to get inspiration from:
https://www.brightvalen.example/
https://tavumeq.example/
I will provide the colors and logo soon

Lumoravex.example is our current website

So, in brief, we provide the highest caliber of digital and software consulting services. We are treating this company, not as your run-of-the-mill average digital agency that simply handles media buying. We want to be viewed as a full suite, 360° business solutions, agency that utilizes state of the art, content, writing, media buying, Data analytics, highest converting, landing, pages and designs. We also employ custom software solutions that help to automate and streamline, day-to-day business activities, which cause a lot of and efficiencies, wastage, human error, and most of all losing countless amount of revenue each month. We will have a lot of video testimonials and case studies and references on our website as well as social channels. we will be a very visually driven company that demonstrates our solutions with practical and tangible scenarios which the clients can relate to.

Target Market(s)

Mid market to enterprise companies

Industry/Entity Type

Digital & software consulting

Number of Pages Required

5+ page

Font styles to use
Sans Serif

Colors
0054AA
0677BA
7BADD7
CADEEF
E8F1F8
EE7325
F08F49
F5BC92
FAE3D3
FDF4ED

Requirements
Must have
• Graphic
Nice to have
• Metrics and graphics to show ROI of streamlining business processes to automate, systemize your business via software solutions. Should also have same concept to show why teaming up with a digital agency is important and why the detriment of using an offshore team or lead gen sites like Pelko or drub etc

```html
<!DOCTYPE html>
<html lang="en">
<head>
<meta charset="utf-8">
<title>Lumoravex — Digital &amp; Software Consulting</title>
<link href="https://fonts.googleapis.com/css2?family=Montserrat:wght@500;600;700&family=Raleway:wght@400;500;600&display=swap" rel="stylesheet">
<style>
:root{
  --blue:#2328e6;
  --blue-deep:#1b20c9;
  --cyan:#1ec8f5;
  --ink:#222;
  --muted:#777;
  --white:#fff;
  --dark:#101018;
}
*{box-sizing:border-box;margin:0;padding:0}
html,body{width:1200px;height:5186px;overflow:hidden}
body{position:relative;background:var(--white);font-family:"Raleway",sans-serif;color:var(--ink)}
.abs{position:absolute}
h1,h2,h3,.mont{font-family:"Montserrat",sans-serif}

/* header */
.site-header{left:0;top:0;width:1200px;height:100px;background:var(--white);z-index:2}
.brand{left:111px;top:24px;display:flex;align-items:center;gap:10px}
.brand-mark{width:44px;height:44px;border-radius:50%;background:var(--blue)}
.brand-name{font-family:"Montserrat",sans-serif;font-weight:700;font-size:32px;color:var(--blue);line-height:1}
.brand-tag{font-family:"Montserrat",sans-serif;font-weight:700;font-size:9px;color:var(--ink);letter-spacing:.5px;margin-top:3px}
.nav{left:446px;top:38px;display:flex;gap:24px;font-family:"Montserrat",sans-serif;font-weight:600;font-size:14px}
.nav a{color:var(--ink);text-decoration:none}
.nav a.active{color:var(--blue);border-bottom:2px solid var(--blue);padding-bottom:4px}

/* hero */
.hero{left:0;top:100px;width:1200px;height:689px;overflow:hidden;background:linear-gradient(180deg,#f7f8f9 0%,#eef0f2 45%,#e2e5e8 100%)}
.hero-scene{left:300px;top:340px;width:640px;height:340px;filter:blur(28px);opacity:.9;
  background:linear-gradient(90deg,#d9c3ad 0%,#2f3c58 14%,#e3d5c6 28%,#3b4660 40%,#f0ece6 52%,#c9b09a 62%,#2b3650 76%,#d6c0aa 88%,#e9e9ea 100%)}
.hero-desk{left:240px;top:610px;width:760px;height:80px;background:linear-gradient(180deg,#d7dade,#c3c7cc);filter:blur(10px)}
.hero-title{left:0;top:262px;width:1200px;text-align:center;font-size:50px;font-weight:600;line-height:52px;color:#111;z-index:1}
.btn{display:inline-flex;align-items:center;gap:6px;font-family:"Montserrat",sans-serif;font-weight:600;font-size:13px;border-radius:22px;text-decoration:none}
.btn-hero{left:518px;top:396px;width:164px;height:42px;justify-content:center;background:var(--blue);color:#fff;z-index:1}
.round-arrow{width:44px;height:44px;border-radius:50%;background:rgba(90,90,90,.75);display:flex;align-items:center;justify-content:center;z-index:1}

/* partner */
.partner{left:0;top:789px;width:1200px;height:515px;background:var(--blue)}
.partner-title{left:111px;top:862px;font-size:41px;font-weight:600;color:#fff}
.partner-text{left:111px;top:930px;width:978px;font-size:13px;line-height:21px;color:#fff}
.partner-text p+p{margin-top:22px}
.partner-img{left:111px;top:1097px;width:978px;height:344px;box-shadow:0 24px 30px rgba(0,0,0,.12);
  background:
   radial-gradient(ellipse 30% 45% at 72% 55%,rgba(60,70,90,.55),transparent 70%),
   radial-gradient(ellipse 40% 35% at 25% 70%,rgba(170,140,120,.45),transparent 70%),
   linear-gradient(180deg,#f1f0ed 0%,#e4e1dc 45%,#bdb6ad 75%,#8b8378 100%)}

/* section headings */
.divider{width:84px;height:3px;background:var(--blue);left:558px}
.sec-title{left:0;width:1200px;text-align:center;font-size:42px;font-weight:600;line-height:52px;color:var(--ink)}

/* concept cards */
.card{overflow:hidden;box-shadow:0 6px 14px rgba(0,0,0,.15)}
.card-img{width:100%;height:100%}
.card-img::after{content:"";position:absolute;inset:0;background:linear-gradient(180deg,transparent 55%,rgba(0,0,0,.45) 100%)}
.img-web{background:radial-gradient(ellipse 35% 40% at 45% 30%,#c8643c,transparent 70%),radial-gradient(ellipse 40% 50% at 20% 60%,#35394a,transparent 70%),linear-gradient(160deg,#e7e6e8,#9a9aa3 60%,#4a4d58)}
.img-ecom{background:radial-gradient(ellipse 50% 30% at 60% 20%,#cfe0f2,transparent 70%),radial-gradient(ellipse 35% 40% at 30% 60%,#3d5f8a,transparent 70%),linear-gradient(160deg,#eef2f6,#8ea4bd 55%,#3a4a60)}
.img-dm{background:radial-gradient(ellipse 35% 45% at 60% 40%,#b98a6b,transparent 70%),radial-gradient(ellipse 30% 40% at 15% 55%,#2a2a2e,transparent 70%),linear-gradient(160deg,#d8c3a6,#9b7f62 55%,#4a3a30)}
.img-data{background:radial-gradient(ellipse 35% 40% at 35% 40%,#c9a888,transparent 70%),radial-gradient(ellipse 35% 45% at 75% 55%,#2f3645,transparent 70%),linear-gradient(160deg,#e6ddd2,#a5958a 55%,#4d4640)}
.card-label{position:absolute;left:30px;bottom:50px;font-family:"Montserrat",sans-serif;font-weight:600;font-size:20px;color:#fff;z-index:1}
.card-go{position:absolute;right:30px;bottom:28px;width:50px;height:50px;border-radius:50%;background:var(--blue);display:flex;align-items:center;justify-content:center;z-index:1}

/* IT services */
.services{left:0;top:2524px;width:1200px;height:395px;background:linear-gradient(180deg,var(--blue) 0%,#2a5cf0 60%,#33a4f6 100%)}
.svc{overflow:hidden}
.svc-img{width:100%;height:100%}
.svc-img::after{content:"";position:absolute;inset:0;background:linear-gradient(180deg,transparent 45%,rgba(10,15,30,.6) 100%)}
.svc-1{background:radial-gradient(ellipse 40% 50% at 30% 40%,#4f7fa5,transparent 70%),linear-gradient(180deg,#3b5671,#1f2c3c)}
.svc-2{background:radial-gradient(ellipse 50% 40% at 50% 35%,#b7a896,transparent 70%),linear-gradient(180deg,#6e6258,#2a2622)}
.svc-3{background:radial-gradient(ellipse 45% 40% at 55% 40%,#c2c6cc,transparent 70%),linear-gradient(180deg,#7d8793,#343b45)}
.svc-icon{position:absolute;left:50%;top:160px;transform:translateX(-50%);width:82px;height:82px;border-radius:50%;background:var(--blue);border:4px solid rgba(255,255,255,.35);display:flex;align-items:center;justify-content:center;z-index:1}
.svc-label{position:absolute;left:0;width:100%;top:258px;text-align:center;font-family:"Montserrat",sans-serif;font-weight:600;font-size:18px;color:#fff;z-index:1}

/* testimonial */
.map{left:290px;top:3290px;width:870px;height:560px;background:radial-gradient(ellipse at center,#eef0f2 0%,#f6f7f8 55%,#fff 80%)}
.video{left:111px;top:3321px;width:420px;height:314px;border-radius:6px;
  background:radial-gradient(ellipse 25% 35% at 30% 55%,#6b4f3e,transparent 70%),radial-gradient(ellipse 25% 40% at 62% 45%,#2d3a55,transparent 70%),radial-gradient(ellipse 20% 30% at 82% 65%,#9a6f55,transparent 70%),linear-gradient(180deg,#dfe6ee,#a8b6c6 50%,#6d7b8c)}
.play{left:282px;top:3443px;width:74px;height:74px;border-radius:50%;background:var(--cyan);display:flex;align-items:center;justify-content:center}
.quote-mark{font-family:"Montserrat",sans-serif;font-size:200px;color:#e4e4e4;line-height:1}
.quote{left:644px;top:3360px;width:398px;font-size:13px;line-height:26px;color:var(--muted);text-align:justify}
.client-badge{left:800px;top:3521px;width:86px;height:86px;border-radius:50%;border:3px solid #111;background:#fff;display:flex;align-items:center;justify-content:center}
.client-badge span{width:40px;height:40px;border-radius:50%;background:var(--cyan)}
.client-name{left:743px;top:3636px;width:200px;text-align:center;font-size:15px;font-weight:500}
.dot{width:12px;height:12px;border-radius:50%;background:#3aa0f0;box-shadow:0 0 0 6px rgba(58,160,240,.15)}

/* case study */
.case{width:230px}
.case-icon{width:112px;height:112px;border-radius:50%;display:flex;align-items:center;justify-content:center}
.case h3{margin-top:22px;font-size:19px;font-weight:600}
.case p{margin-top:10px;font-size:13px;line-height:21px;color:var(--muted)}
.case-more{margin-top:18px;width:36px;height:36px;border-radius:50%;background:#ececec;display:flex;align-items:center;justify-content:center;color:#777;font-size:14px}

/* cta + footer */
.footer{left:0;top:4565px;width:1200px;height:621px;background:var(--dark)}
.cta{left:111px;top:4412px;width:978px;height:266px;
  background:radial-gradient(ellipse 12% 40% at 20% 100%,#0d1170,transparent 70%),radial-gradient(ellipse 12% 45% at 45% 100%,#0d1170,transparent 70%),radial-gradient(ellipse 14% 45% at 75% 100%,#0d1170,transparent 70%),linear-gradient(180deg,var(--blue) 0%,var(--blue-deep) 100%)}
.cta-title{left:0;top:4455px;width:1200px;text-align:center;font-size:42px;font-weight:600;line-height:52px;color:#fff}
.btn-cta{left:517px;top:4573px;width:166px;height:42px;justify-content:center;background:#fff;color:var(--blue)}
.f-title{font-family:"Montserrat",sans-serif;font-weight:500;font-size:19px;color:#fff}
.field{background:#fff;height:36px;font-size:12px;color:#888;padding:10px 18px}
.btn-submit{left:111px;top:5006px;width:134px;height:42px;justify-content:center;background:var(--blue);color:#fff}
.links{list-style:none;font-size:14px;color:#fff}
.links li{height:30px;display:flex;gap:14px;align-items:center}
.links li::before{content:"»";font-size:13px}
.contact-row{display:flex;gap:14px;font-size:14px;color:#fff;line-height:22px}
.social{width:30px;height:30px;border-radius:50%}
.copy{left:0;top:5122px;width:1200px;text-align:center;font-size:14px;color:#fff}
</style>
</head>
<body>

<header class="site-header abs">
  <div class="brand abs">
    <span class="brand-mark"></span>
    <div>
      <div class="brand-name">Lumoravex</div>
      <div class="brand-tag">DIGITAL &amp; SOFTWARE CONSULTING</div>
    </div>
  </div>
  <nav class="nav abs">
    <a class="active" href="#">Home</a><a href="#">About Us</a><a href="#">Web Development</a><a href="#">Digital Marketing</a><a href="#">IT Solutions</a><a href="#">Connect Us</a>
  </nav>
</header>

<section class="hero abs" role="img" aria-label="Team of five business people gathered around a laptop in a bright office">
  <div class="hero-scene abs"></div>
  <div class="hero-desk abs"></div>
</section>
<h1 class="hero-title abs">Systemize Your Business<br>Via Software Solutions</h1>
<a class="btn btn-hero abs">GET STATRTED
  <svg width="14" height="14" viewBox="0 0 14 14"><circle cx="7" cy="7" r="7" fill="#fff"/><path d="M6 4l3 3-3 3" stroke="#2328e6" stroke-width="1.8" fill="none"/></svg></a>
<div class="round-arrow abs" style="left:33px;top:438px"><svg width="12" height="12"><path d="M8 2L4 6l4 4" stroke="#fff" stroke-width="1.6" fill="none"/></svg></div>
<div class="round-arrow abs" style="left:1125px;top:438px"><svg width="12" height="12"><path d="M4 2l4 4-4 4" stroke="#fff" stroke-width="1.6" fill="none"/></svg></div>

<section class="partner abs"></section>
<svg class="abs" style="left:40px;top:1080px" width="200" height="240" viewBox="0 0 200 240"><path d="M190 10 A150 150 0 0 0 20 230" stroke="#1ec8f5" stroke-width="22" fill="none"/></svg>
<h2 class="partner-title abs">Your Partner for Software Innovation</h2>
<div class="partner-text abs">
  <p>At Lumoravex we aspire to be an integrated and innovative partner with a passion for providing solutions that help deliver positive results for our clients. We want to understand your business, target audience and objectives online. So that, we can design and implement solutions that speaks to your audience. Our 'educate approach' will provide you a full understanding of all options available, so you can make the best decision.</p>
  <p>Our team are specialists in their field, each as passionate about digital marketing, website development and custom software solutions as the next. Everything we deliver for you is created in-house by our people from design and developing to SEO and business branding.</p>
</div>
<div class="partner-img abs" role="img" aria-label="Presenter leading a workshop with colleagues seated around a meeting table"></div>

<div class="divider abs" style="top:1531px"></div>
<h2 class="sec-title abs" style="top:1548px">Design the Concept<br>of Your Business Idea Now</h2>

<div class="card abs" style="left:111px;top:1675px;width:473px;height:348px"><div class="card-img img-web" role="img" aria-label="Developers discussing work at a laptop"></div><span class="card-label">Web Development</span><span class="card-go"><svg width="28" height="20"><path d="M2 10h22M16 3l8 7-8 7" stroke="#fff" stroke-width="2.5" fill="none"/></svg></span></div>
<div class="card abs" style="left:614px;top:1675px;width:473px;height:348px"><div class="card-img img-ecom" role="img" aria-label="Team reviewing charts on a whiteboard"></div><span class="card-label">E-Commerce Website</span><span class="card-go"><svg width="28" height="20"><path d="M2 10h22M16 3l8 7-8 7" stroke="#fff" stroke-width="2.5" fill="none"/></svg></span></div>
<div class="card abs" style="left:111px;top:2053px;width:473px;height:348px"><div class="card-img img-dm" role="img" aria-label="Content creator recording a video in front of a camera"></div><span class="card-label">Digital Marketing</span><span class="card-go"><svg width="28" height="20"><path d="M2 10h22M16 3l8 7-8 7" stroke="#fff" stroke-width="2.5" fill="none"/></svg></span></div>
<div class="card abs" style="left:614px;top:2053px;width:473px;height:348px"><div class="card-img img-data" role="img" aria-label="Colleagues smiling while analysing data on a laptop"></div><span class="card-label">Data Analytics</span><span class="card-go"><svg width="28" height="20"><path d="M2 10h22M16 3l8 7-8 7" stroke="#fff" stroke-width="2.5" fill="none"/></svg></span></div>

<section class="services abs"></section>
<div class="abs" style="left:0;top:2919px;width:1200px;height:130px;background:#fff"></div>
<div class="divider abs" style="top:2586px;background:#fff"></div>
<h2 class="sec-title abs" style="top:2601px;color:#fff">We Offer a Wide<br>Variety of IT Services</h2>
<svg class="abs" style="left:108px;top:2848px" width="30" height="42"><path d="M24 2L6 21l18 19" stroke="#fff" stroke-width="3" fill="none"/></svg>
<svg class="abs" style="left:108px;top:2943px" width="30" height="42"><path d="M6 2l18 19-18 19" stroke="#111" stroke-width="3" fill="none"/></svg>
<div class="svc abs" style="left:215px;top:2744px;width:277px;height:302px"><div class="svc-img svc-1" role="img" aria-label="Two engineers examining a wall of data screens"></div>
  <span class="svc-icon"><svg width="36" height="36" viewBox="0 0 36 36" fill="none" stroke="#fff" stroke-width="2"><circle cx="18" cy="18" r="6"/><path d="M18 4v5M18 27v5M4 18h5M27 18h5M8 8l3.5 3.5M24.5 24.5L28 28M8 28l3.5-3.5M24.5 11.5L28 8"/></svg></span><span class="svc-label">Web Development</span></div>
<div class="svc abs" style="left:513px;top:2744px;width:277px;height:302px"><div class="svc-img svc-2" role="img" aria-label="Hands typing on a laptop keyboard"></div>
  <span class="svc-icon"><svg width="36" height="36" viewBox="0 0 36 36" fill="none" stroke="#fff" stroke-width="2"><circle cx="18" cy="18" r="13"/><circle cx="18" cy="18" r="8"/><circle cx="18" cy="18" r="3"/></svg></span><span class="svc-label">Software Solutions</span></div>
<div class="svc abs" style="left:811px;top:2744px;width:277px;height:302px"><div class="svc-img svc-3" role="img" aria-label="Designer reviewing interface charts on paper"></div>
  <span class="svc-icon"><svg width="36" height="36" viewBox="0 0 36 36" fill="none" stroke="#fff" stroke-width="2"><circle cx="18" cy="18" r="13"/><path d="M5 18h26M18 5c-6 7-6 19 0 26M18 5c6 7 6 19 0 26"/></svg></span><span class="svc-label">UI/UX Design</span></div>

<div class="divider abs" style="top:3141px"></div>
<h2 class="sec-title abs" style="top:3159px">We are Trusted<br>4+ Countries Worldwide</h2>
<div class="map abs" role="img" aria-label="Faint world map background"></div>
<span class="dot abs" style="left:776px;top:3302px"></span>
<span class="dot abs" style="left:1078px;top:3482px"></span>
<span class="dot abs" style="left:354px;top:3773px"></span>
<span class="dot abs" style="left:678px;top:3750px"></span>
<div class="video abs" role="img" aria-label="Video testimonial still of a smiling client team in an office"></div>
<div class="play abs"><svg width="26" height="28"><path d="M4 2l20 12L4 26z" fill="#fff"/></svg></div>
<div class="quote-mark abs" style="left:563px;top:3270px">“</div>
<div class="quote-mark abs" style="left:990px;top:3445px">”</div>
<p class="quote abs">"We thank Lumoravex for the wonderful job in helping us develop our E - Commerce Store. Everyone was professional, excellent and hard working. Thanks to them, we were able to achieve our goal on time, and we look forward to continue working with them in the future."</p>
<div class="client-badge abs"><span></span></div>
<div class="client-name abs">Cartwell</div>
<div class="round-arrow abs" style="left:33px;top:3467px;background:#777"><svg width="12" height="12"><path d="M8 2L4 6l4 4" stroke="#fff" stroke-width="1.6" fill="none"/></svg></div>
<div class="round-arrow abs" style="left:1125px;top:3467px;background:#777"><svg width="12" height="12"><path d="M4 2l4 4-4 4" stroke="#fff" stroke-width="1.6" fill="none"/></svg></div>

<div class="divider abs" style="top:3870px"></div>
<h2 class="sec-title abs" style="top:3887px">Case Study</h2>
<div class="case abs" style="left:111px;top:3990px"><div class="case-icon" style="background:var(--blue)"><svg width="50" height="50" viewBox="0 0 50 50" fill="none" stroke="#fff" stroke-width="2.5"><rect x="6" y="10" width="30" height="32"/><path d="M12 36v-8M18 36v-12M24 36v-6"/><circle cx="32" cy="18" r="8"/><path d="M38 24l7 7"/></svg></div><h3>Lorem ipsum dolor</h3><p>Lorem ipsum dolor sit amet, con sectetur adipiscing elit, sed do ei usmod tempor incididunt ut lab ore et dolore magna aliqua.</p><div class="case-more">»</div></div>
<div class="case abs" style="left:363px;top:3990px"><div class="case-icon" style="background:var(--cyan)"><svg width="50" height="50" viewBox="0 0 50 50" fill="none" stroke="#fff" stroke-width="2.5"><rect x="6" y="14" width="38" height="28" rx="3"/><path d="M18 14V9h14v5M6 26h38M22 26v5h6v-5"/></svg></div><h3>Lorem ipsum dolor</h3><p>Lorem ipsum dolor sit amet, con sectetur adipiscing elit, sed do ei usmod tempor incididunt ut lab ore et dolore magna aliqua.</p><div class="case-more">»</div></div>
<div class="case abs" style="left:614px;top:3990px"><div class="case-icon" style="background:var(--blue)"><svg width="50" height="50" viewBox="0 0 50 50" fill="none" stroke="#fff" stroke-width="2.5"><rect x="14" y="6" width="22" height="28" rx="2"/><path d="M19 14h12M19 20h12M19 26h8"/><path d="M6 36c8-2 14 6 22 4l14-6"/></svg></div><h3>Lorem ipsum dolor</h3><p>Lorem ipsum dolor sit amet, con sectetur adipiscing elit, sed do ei usmod tempor incididunt ut lab ore et dolore magna aliqua.</p><div class="case-more">»</div></div>
<div class="case abs" style="left:866px;top:3990px"><div class="case-icon" style="background:var(--cyan)"><svg width="50" height="50" viewBox="0 0 50 50" fill="none" stroke="#fff" stroke-width="2.5"><circle cx="18" cy="18" r="8"/><circle cx="18" cy="18" r="3"/><circle cx="30" cy="30" r="9"/><path d="M36 36l8 8"/></svg></div><h3>Lorem ipsum dolor</h3><p>Lorem ipsum dolor sit amet, con sectetur adipiscing elit, sed do ei usmod tempor incididunt ut lab ore et dolore magna aliqua.</p><div class="case-more">»</div></div>

<footer class="footer abs"></footer>
<div class="cta abs" role="img" aria-label="Silhouettes of a team in a meeting, tinted blue"></div>
<h2 class="cta-title abs">We are Trusted<br>4+ Countries Worldwide</h2>
<a class="btn btn-cta abs">CONTACT US
  <svg width="14" height="14" viewBox="0 0 14 14"><circle cx="7" cy="7" r="7" fill="#2328e6"/><path d="M6 4l3 3-3 3" stroke="#fff" stroke-width="1.8" fill="none"/></svg></a>

<div class="f-title abs" style="left:111px;top:4766px">GET IN TOUCH</div>
<div class="field abs" style="left:111px;top:4815px;width:236px">First Name</div>
<div class="field abs" style="left:353px;top:4815px;width:236px">Last Name</div>
<div class="field abs" style="left:111px;top:4863px;width:236px">Email</div>
<div class="field abs" style="left:353px;top:4863px;width:236px">phone number</div>
<div class="field abs" style="left:111px;top:4913px;width:478px;height:76px">Message</div>
<a class="btn btn-submit abs">SUBMIT</a>

<div class="f-title abs" style="left:674px;top:4766px">QUICK LINKS</div>
<ul class="links abs" style="left:674px;top:4800px">
  <li>Home</li><li>About Us</li><li>Blog</li><li>Our Services</li><li>Testimonials</li><li>Contact Us</li>
</ul>

<div class="f-title abs" style="left:896px;top:4766px">CONTACT US</div>
<div class="contact-row abs" style="left:898px;top:4812px"><svg width="12" height="16"><path d="M6 15C2 10 1 8 1 6a5 5 0 0110 0c0 2-1 4-5 9z" fill="#fff"/><circle cx="6" cy="6" r="2" fill="#101018"/></svg><span>USA: 1200 Harbor Lane<br>&nbsp;&nbsp;&nbsp;&nbsp;&nbsp;&nbsp;Fremont, CA 94000</span></div>
<div class="contact-row abs" style="left:898px;top:4890px"><svg width="12" height="16"><rect x="2" y="1" width="8" height="14" rx="1.5" fill="none" stroke="#fff" stroke-width="1.6"/></svg><span>+1 555 010 2040</span></div>
<div class="contact-row abs" style="left:896px;top:4931px"><svg width="14" height="14"><rect x="1" y="2" width="12" height="10" fill="none" stroke="#fff" stroke-width="1.5"/><path d="M1 3l6 5 6-5" stroke="#fff" stroke-width="1.3" fill="none"/></svg><span>info@lumoravex.example</span></div>

<div class="abs mont" style="left:674px;top:5022px;font-size:17px;font-weight:600;color:#fff">STAY CONNECTED :</div>
<span class="social abs" style="left:876px;top:5017px;background:#3b5bd6"></span>
<span class="social abs" style="left:914px;top:5017px;background:#d6337a"></span>

<div class="copy abs">© 2023 Company Name &nbsp;| All Rights Reserved | Terms and Conditions</div>

</body>
</html>
```